Marisol Lodge website redesign

After 8 years of our current site, we're ready to upgrade our site design. We'd like to generally make it more modern and clean and build it on a CMS like joomla for easier future maintenance.

Our hotel is a family-owned bed and breakfast that competes against much larger hotel chains in Aspen with fancier rooms and larger pricetags. Our hotel is priced moderately and features tasteful, uniquely-design rooms.

We are looking for a website that will showcase the uniqueness of our rooms, the history of the Lodge, and the friendliness of our staff.

Here are some other hotel sites we like:

http://www.thecopperwren.example/

http://www.pinecrestridgehouse.example/

http://www.hotelbrivaro.example/

*********

Scope of Work - I'm looking for a design AND build. The website should be built out in Joomla as part of the final deliverable.

Current website: http://www.marisollodge.example/

Explanation of what design + build means:

I am looking for not only the design of the site, but also for the homepage and one subpage to be built out as well. I do NOT need the entire site built - only for those two pages to be built and I will retrofit the remainder of the pages.

Target Market(s)

travellers evaluating hotels in Aspen, Colorado.

Industry/Entity Type

Hotel

Requirements
Must have
• Must, must, must be based on a joomla template. "Rotating" large main image as central position on homepage is a must (see example websites mentioned above).

Nice to have
• We have an existing online reservation system. It would be nice to evaluate placing a "widget" on the homepage that integrates to the online reservation page. Similar to that feature that the Copper Wren website has at the foot of the main image on their homepage.

```html
<!DOCTYPE html>
<html lang="en">
<head>
<meta charset="utf-8">
<title>Marisol Lodge</title>
<link rel="stylesheet" href="https://fonts.googleapis.com/css2?family=Cabin:wght@400;500&family=Merienda:wght@400&display=swap">
<style>
  :root {
    --olive: #959f00;
    --olive-dark: #4b5300;
    --header-bg: #f1f1f1;
    --nav-text: #1f2100;
    --ink: #333333;
    --heading-grey: #5a5a5a;
    --heading-green: #7b9a00;
    --book-red: #c4000b;
    --field-dark: #2b2b2b;
    --bar-grey: rgba(110,110,110,0.78);
    --search-top: #ff9a1a;
    --search-bottom: #e04a00;
    --footer-copy: #7a7f20;
  }
  * { box-sizing: border-box; margin: 0; padding: 0; }
  html, body { width: 1200px; height: 1000px; overflow: hidden; background: #fff; }
  body { font-family: 'Cabin', sans-serif; color: var(--ink); position: relative; }

  .site-header { position: absolute; left: 0; top: 0; width: 1200px; height: 184px;
    background: var(--header-bg); }
  .brand-tab { position: absolute; left: 0; top: 0; }
  .brand-name { position: absolute; left: 393px; width: 410px; top: 64px; text-align: center;
    font-family: 'Cabin', sans-serif; font-weight: 400; font-size: 42px; color: #fff; }

  .main-nav { position: absolute; left: 0; top: 132px; width: 1200px; height: 52px;
    background: var(--olive); border-top: 3px solid var(--olive-dark); border-bottom: 4px solid #111; }
  .main-nav ul { list-style: none; display: flex; justify-content: center; gap: 50px;
    padding-top: 16px; margin-left: 6px; }
  .main-nav a { font-size: 15px; color: var(--nav-text); text-decoration: none; }

  .hero { position: absolute; left: 0; top: 184px; width: 1200px; height: 557px;
    background: linear-gradient(180deg, #c9d8e2 0%, #b8a98a 22%, #4f7a2c 45%, #6e9a36 65%, #8a8a78 85%, #5c6a70 100%); }
  .hero-arrow { position: absolute; top: 254px; width: 48px; height: 48px; border-radius: 50%;
    background: rgba(30,30,30,0.75); border: 2px solid rgba(200,200,200,0.6); }
  .hero-arrow.prev { left: 166px; }
  .hero-arrow.next { left: 988px; }
  .hero-arrow svg { position: absolute; left: 12px; top: 11px; }

  .booking-bar { position: absolute; left: 194px; top: 478px; width: 808px; height: 53px;
    background: var(--bar-grey); }
  .book-now { position: absolute; left: 0; top: 0; width: 129px; height: 53px; background: var(--book-red);
    color: #fff; font-size: 18px; line-height: 53px; text-align: center; }
  .field { position: absolute; top: 16px; height: 20px; background: var(--field-dark); color: #fff;
    font-size: 11px; line-height: 20px; padding-left: 4px; border: 1px solid #555; }
  .cal { position: absolute; top: 16px; width: 22px; height: 20px; background: #fff; border: 1px solid #aaa; }
  .cal::before { content: ""; position: absolute; left: 2px; right: 2px; top: 2px; height: 4px; background: #1a9ad6; }
  .cal::after { content: ""; position: absolute; left: 4px; right: 4px; top: 8px; bottom: 3px;
    background: repeating-linear-gradient(90deg, #999 0 2px, transparent 2px 4px); }
  .select::after { content: ""; position: absolute; right: 0; top: 0; width: 16px; height: 18px; background: #111; }
  .select::before { content: ""; position: absolute; right: 4px; top: 7px; z-index: 1;
    border-left: 4px solid transparent; border-right: 4px solid transparent; border-top: 5px solid #fff; }
  .divider { position: absolute; left: 397px; top: 0; width: 1px; height: 53px; background: rgba(60,60,60,0.5); }
  .search-btn { position: absolute; left: 717px; top: 16px; width: 74px; height: 24px;
    background: linear-gradient(180deg, var(--search-top), var(--search-bottom)); color: #fff;
    font-size: 12px; line-height: 24px; text-align: center; border-radius: 2px; }

  .welcome { position: absolute; left: 0; top: 741px; width: 1200px; height: 209px; }
  .welcome-title { position: absolute; left: 0; width: 1200px; top: 14px; text-align: center;
    font-family: 'Merienda', cursive; font-weight: 400; font-size: 29px; color: var(--heading-grey); }
  .welcome-title span { color: var(--heading-green); }
  .rule { position: absolute; top: 47px; height: 1px; background: #9a9a9a; }
  .rule.left { left: 215px; width: 150px; }
  .rule.right { left: 820px; width: 165px; }
  .welcome p { position: absolute; left: 195px; width: 810px; text-align: center; font-size: 12.4px; line-height: 18px; color: var(--ink); }
  .intro-a { top: 77px; }
  .intro-b { top: 131px; }

  .site-footer { position: absolute; left: 0; top: 950px; width: 1200px; height: 50px; background: var(--olive); text-align: center; }
  .footer-links { padding-top: 12px; font-size: 9.5px; color: #fff; letter-spacing: 0.2px; }
  .footer-links a { color: #fff; text-decoration: none; }
  .copyright { font-family: Arial, sans-serif; font-size: 10px; color: var(--footer-copy); margin-top: 6px; }
</style>
</head>
<body>
  <header class="site-header">
    <svg class="brand-tab" width="1200" height="140" viewBox="0 0 1200 140" aria-hidden="true">
      <path d="M393 134 L393 78 Q393 40 440 34 L560 32 Q585 30 600 10 Q615 30 640 32 L760 34 Q803 40 803 78 L803 134 Z"
            fill="#959f00" stroke="#4b5300" stroke-width="4"/>
    </svg>
    <div class="brand-name">Marisol Lodge</div>
    <nav class="main-nav">
      <ul>
        <li><a href="#">About The Lodge</a></li>
        <li><a href="#">Rooms</a></li>
        <li><a href="#">Amenities</a></li>
        <li><a href="#">Reservations</a></li>
        <li><a href="#">Aspen Information</a></li>
        <li><a href="#">Manager's Journal</a></li>
      </ul>
    </nav>
  </header>

  <section class="hero" role="img" aria-label="Rotating photo of a stately stone manor with formal gardens, clipped hedges and a fountain in the foreground">
    <div class="hero-arrow prev"><svg width="20" height="22" viewBox="0 0 20 22"><path d="M14 2 L5 11 L14 20" fill="none" stroke="#ccc" stroke-width="2"/></svg></div>
    <div class="hero-arrow next"><svg width="20" height="22" viewBox="0 0 20 22"><path d="M6 2 L15 11 L6 20" fill="none" stroke="#ccc" stroke-width="2"/></svg></div>

    <form class="booking-bar">
      <div class="book-now">BOOK NOW</div>
      <div class="field" style="left:145px;width:85px;">Check in</div>
      <div class="cal" style="left:233px;"></div>
      <div class="field" style="left:272px;width:84px;">Check Out</div>
      <div class="cal" style="left:359px;"></div>
      <div class="divider"></div>
      <div class="field select" style="left:415px;width:85px;">No. Adult</div>
      <div class="field select" style="left:517px;width:86px;">No. Rooms</div>
      <div class="field select" style="left:619px;width:85px;">No. Night</div>
      <div class="search-btn">SEARCH</div>
    </form>
  </section>

  <section class="welcome">
    <div class="rule left"></div>
    <h1 class="welcome-title">Welcome to <span>Marisol Lodge</span></h1>
    <div class="rule right"></div>
    <p class="intro-a">Located in the heart of downtown Aspen, the newly renovated Marisol Lodge possesses all the charms of a vintage European Ski Lodge, while offering all of the modern conveniences one would expect with a stay in Aspen.</p>
    <p class="intro-b">A stay at our lodge includes free continental breakfast in our dining room, daily maid service, free wireless internet access, and a fully-equipped conference facility. Guests are also invited to relax in one of our two outdoor Jacuzzis or in our lounge, where a 42-inch plasma TV and fireplace make for a pleasant area to unwind.</p>
  </section>

  <footer class="site-footer">
    <div class="footer-links"><a href="#">CONTACT</a> | <a href="#">BEST RATE</a> | <a href="#">GUARANTEE</a> | <a href="#">PRIVACY SITE</a> | <a href="#">MAP</a> | <a href="#">BLOG MEDIA</a></div>
    <div class="copyright">Copyright 2012 Marisol Lodge. All Rights Reserved.</div>
  </footer>
</body>
</html>
```